Wordpress Design Project - QuorvanLabs

I would like our existing old website at www.quorvanlabs.example to be redesigned to a more modern attractive site using Wordpress, a total of 5 web pages. And also installed onto our new web hosting site. Please visit the existing website using Microsoft Internet explorer to see the content.
The new site must be compatible with all popular web browsers and mobile devices (if possible).
There should be a contact button available on each page with an associated form in case an interested person wants to contact us. This form must be spam proof not allowing automated crawlers from activating it.
Updates

There are only 5 pages web pages to this QuorvanLabs project.

Industry/Entity Type

Internet

```html
<!DOCTYPE html>
<html lang="en">
<head>
<meta charset="utf-8">
<title>QuorvanLabs</title>
<link rel="stylesheet" href="https://fonts.googleapis.com/css2?family=Open+Sans:wght@400;600;700&display=swap">
<style>
:root{
  --blue:#0d4b91;
  --blue-light:#1f5fa8;
  --text:#6a6a6a;
  --dark:#333;
  --bg:#f1f1f1;
  --panel:#3d3d3d;
  --footer:#4a4a4a;
  --rule:#c9c9c9;
}
*{box-sizing:border-box;margin:0;padding:0}
html,body{width:1200px;height:1153px;overflow:hidden}
body{position:relative;background:var(--bg);font-family:"Open Sans",Arial,sans-serif;color:var(--text);border-top:5px solid var(--blue)}
.abs{position:absolute}
.brand{left:130px;top:25px;display:flex;align-items:center;gap:14px}
.brand-dot{width:56px;height:56px;border-radius:50%;background:var(--blue)}
.brand-name{font-size:30px;font-weight:700;color:var(--blue)}
.call{left:712px;top:24px}
.mail{left:895px;top:24px}
.label{font-size:17px;color:var(--blue)}
.phone{font-size:21px;font-weight:600;color:#666;margin-top:2px;letter-spacing:.5px}
.email{font-size:12px;color:#666;margin-top:8px}
.nav-rule{left:130px;top:123px;width:940px;height:4px;background:var(--rule)}
.nav-pointer{left:148px;top:127px;width:0;height:0;border-left:11px solid transparent;border-right:11px solid transparent;border-top:10px solid var(--rule)}
.nav{left:141px;top:140px;display:flex;font-size:13px;color:#333}
.nav span{margin-right:0}
.banner-frame{left:130px;top:177px;width:940px;height:344px;background:#fff;border:1px solid #ddd;box-shadow:0 12px 14px -10px rgba(0,0,0,.35)}
.banner-photo{position:absolute;left:3px;top:3px;width:934px;height:338px;background:linear-gradient(90deg,#7f7b91 0%,#8a879b 40%,#c9c8d2 62%,#e2e2e8 80%,#cfcfd6 100%)}
.banner-text{position:absolute;left:28px;top:64px;font-size:31px;line-height:41px;font-weight:600;color:#fff;text-shadow:0 1px 2px rgba(0,0,0,.35)}
.dots{position:absolute;left:28px;top:298px;display:flex;gap:8px}
.dots i{width:18px;height:18px;background:#4a6394;border-radius:2px}
.dots i:first-child{background:var(--blue)}
h2{font-weight:400;font-size:23px;color:var(--blue)}
.welcome{left:130px;top:542px;width:680px}
p{font-size:12.5px;line-height:20px}
.more{left:131px;top:693px;font-size:12px;font-weight:600;color:#333}
.dash{left:130px;top:733px;width:685px;border-top:1px dashed #bbb}
.support{left:130px;top:751px;width:690px}
.col-title{font-size:14px;font-weight:600;color:#333}
.list{list-style:none;margin-top:10px}
.list li{font-size:12.5px;color:var(--blue-light);height:28px;padding-left:20px;position:relative}
.list li::before{content:"";position:absolute;left:0;top:5px;border-left:6px solid #555;border-top:4px solid transparent;border-bottom:4px solid transparent}
.quick{left:850px;top:548px;width:220px;height:472px;border-radius:4px;background:linear-gradient(#474747,#363636);color:#eee;padding:14px 20px}
.quick h3{font-weight:400;font-size:22px;color:#fff}
.field-label{font-size:12px;position:absolute;left:20px}
.field{position:absolute;left:20px;width:184px;height:31px;background:#fff;border:1px solid #ccc;border-radius:3px}
.captcha{position:absolute;left:20px;top:391px;width:88px;height:25px;background:linear-gradient(90deg,#ddd,#bbb,#ddd)}
.captcha-input{position:absolute;left:113px;top:391px;width:89px;height:25px;background:#fff}
.submit{position:absolute;left:125px;top:428px;width:77px;height:27px;background:var(--blue);color:#fff;font-size:13px;font-weight:600;text-align:center;line-height:27px;border:1px solid #5a7fb5}
.footer{left:0;top:1036px;width:1200px;height:117px;background:var(--footer);color:#ddd}
.foot-nav{position:absolute;left:130px;top:31px;font-size:11px;color:#ddd;word-spacing:2px}
.copy{position:absolute;left:130px;top:71px;font-size:11px;color:#bbb}
.follow{position:absolute;left:929px;top:46px;font-size:13px;font-weight:600;display:flex;gap:8px;align-items:center}
.follow i{width:17px;height:17px;background:#2f7ac8}
</style>
</head>
<body>
<div class="abs brand"><span class="brand-dot"></span><span class="brand-name">QuorvanLabs</span></div>
<div class="abs call"><div class="label">Call Us:</div><div class="phone">1.800.555.0142</div></div>
<div class="abs mail"><div class="label">Email:</div><div class="email">hello@quorvanlabs.example</div></div>
<div class="abs nav-rule"></div>
<div class="abs nav-pointer"></div>
<nav class="abs nav">
  <span style="width:88px">Home</span><span style="width:108px">About Us</span><span style="width:160px">Support Services</span><span style="width:208px">Telephone VoIP&nbsp; Solution</span><span style="width:177px">IP, LAN and Internet</span><span>Contact Us</span>
</nav>
<div class="abs banner-frame">
  <div class="banner-photo" role="img" aria-label="Photo of a white telephone handset resting on large black WWW letters with a coiled cord"></div>
  <div class="banner-text">We provides complete<br>telephone VoIP PBX<br>solutions for businesses<br>large and small.</div>
  <div class="dots"><i></i><i></i><i></i><i></i></div>
</div>
<section class="abs welcome">
  <h2>Welcome to Our Site</h2>
  <p style="margin-top:10px">QuorvanLabs provides complete telephone VoIP PBX solutions for businesses large and small.</p>
  <p style="margin-top:8px">Our team of telecom engineers will design and install the best business telephone VoIP PBX solution for your requirements.&nbsp; System features include: standard and advanced PBX call control actions, video telephone calling, toll free calling any where in the world, and 24x7 support.</p>
</section>
<div class="abs more">MORE DETAILS -&gt;&gt;</div>
<div class="abs dash"></div>
<section class="abs support">
  <h2>Support &amp; Services</h2>
  <p style="margin-top:8px">QuorvanLabs provides full 24 x 7 Internet Access help desk / technical support services for the hospitality industry.</p>
  <div style="display:flex;margin-top:16px">
    <div style="width:380px">
      <div class="col-title">Services features include:</div>
      <ul class="list">
        <li>24 x&nbsp; 365 live, immediate, telephone technical support</li>
        <li>All support personnel are university or college graduates</li>
        <li>All support personnel are located in USA or Canada</li>
        <li>Flat monthly fee</li>
        <li>All Windows and Mac based computers supported</li>
      </ul>
    </div>
    <div>
      <div class="col-title">Help desk / technical support available for:</div>
      <ul class="list">
        <li>Business IP PBX telephone systems</li>
        <li>Internet Access networks</li>
        <li>Wired IT networks</li>
        <li>Wireless IT networks including 802.11a/b/g</li>
        <li>Fiber optic networks</li>
      </ul>
    </div>
  </div>
</section>
<aside class="abs quick">
  <h3>Quick Contact</h3>
  <div class="field-label" style="top:53px">Name</div><div class="field" style="top:73px"></div>
  <div class="field-label" style="top:118px">Email Address</div><div class="field" style="top:139px"></div>
  <div class="field-label" style="top:181px">Contact No.</div><div class="field" style="top:198px"></div>
  <div class="field-label" style="top:242px">Type Message.</div><div class="field" style="top:261px;height:97px"></div>
  <div class="field-label" style="top:369px;font-size:11px">Type the character below given</div>
  <div class="captcha" role="img" aria-label="Distorted verification characters"></div>
  <div class="captcha-input"></div>
  <div class="submit">SUBMIT</div>
</aside>
<footer class="abs footer">
  <div class="foot-nav">Home &nbsp;| &nbsp;About Us &nbsp;| &nbsp;Support Services &nbsp;&nbsp;| &nbsp;&nbsp;Telephone VoIP&nbsp; Solution &nbsp;&nbsp;| &nbsp;&nbsp;IP, LAN and Internet &nbsp;&nbsp;| &nbsp;&nbsp;Contact Us</div>
  <div class="copy">© 2013 QuorvanLabs Inc.</div>
  <div class="follow">Follow Us: <i></i><i></i><i></i></div>
</footer>
</body>
</html>
```